Tech start-up (innovation, industry 4.0, cloud computing) needs a web design+html/css

Company name: Zelmark Technologies

Hi, I need a web design for a tech start-up.

It needs to be mobile, tablet, laptop and monitor friendly

It should contain:
-Logo (in file uploads)
-A header / welcome section, including a language switcher for english and french (I will do the translations myself)
-List of services/products offered
Custom software development
Cloud computing expertise
Consulting
Turn-key solutions

-Fields of expertise
Industry 4.0
Internet of Things (IoT) + Industrial IoT
Automation
Smart manufacturing
Cloud computing
Supply chain integration
Digital twins
-Team
1 member for now
Placeholder photo
Role (President)
Bio (lorem)
Pellorin icon
My GVX certification badge (in file uploads)
Any other field you think is good to have
-Contact form (First name, last name, email, company, subject, i'm not a robot)
-Blog section
-Footer with usual stuff, pellorin icon

I want the design to inspire professionnalism, reliability, excellence but also innovation, invention, creation and dreams of a better future

Inspiration: think about smart factories, robotics, artificial intelligence, cloud computing, high-tech, the future, culture of innovation

If you could make the html+css website that would be great (no wordpress)

```html
<!DOCTYPE html>
<html lang="en">
<head>
<meta charset="utf-8">
<title>Zelmark Technologies</title>
<link href="https://fonts.googleapis.com/css2?family=Poppins:wght@300;400;500;600;700&family=Audiowide&display=swap" rel="stylesheet">
<style>
:root{
  --navy:#0a2748;
  --navy-deep:#061a33;
  --blue:#0e4f8c;
  --sky:#6f9fd2;
  --orange:#ef7d16;
  --orange-deep:#e06a0a;
  --green:#0d8c60;
  --green-deep:#0f6b4c;
  --ink:#111a28;
  --muted:#8a93a0;
  --pale:#e3edf8;
  --pale-2:#f2f7fc;
  --white:#ffffff;
}
*{margin:0;padding:0;box-sizing:border-box}
html,body{width:1200px;height:5249px;overflow:hidden}
body{position:relative;font-family:"Poppins",sans-serif;color:var(--ink);background:var(--white)}
.abs{position:absolute}
a{color:inherit;text-decoration:none}

/* header */
.hero-bg{left:0;top:0;width:1200px;height:620px}
.brand{display:flex;align-items:center;gap:8px;color:var(--orange);font-weight:500}
.brand .dot{width:18px;height:18px;border-radius:50%;background:var(--orange)}
.site-brand{left:153px;top:24px;font-size:20px}
.nav{top:30px;right:150px;display:flex;gap:30px;align-items:center;font-size:10.5px;color:var(--white);font-weight:500}
.flag{width:20px;height:13px;border-radius:2px;background:linear-gradient(135deg,#23408e 0 45%,#fff 45% 55%,#c8102e 55%)}
.hero-title{left:151px;top:216px;color:var(--white);font-size:34px;line-height:50px;font-weight:300}
.hero-title strong{font-weight:600;display:block}
.hero-copy{left:153px;top:330px;width:290px;color:#c7d3e2;font-size:10px;line-height:17px}
.btn{background:var(--blue);color:var(--white);font-size:9px;font-weight:600;text-transform:uppercase;display:flex;align-items:center;justify-content:center;border-radius:20px}
.hero-btn{left:152px;top:410px;width:127px;height:36px}
.hero-art{left:560px;top:165px;width:560px;height:375px;border-radius:18px;background:linear-gradient(160deg,#2d5f96 0%,#5e8fc6 40%,#c8d9ee 70%,#f09140 100%);opacity:.9}

/* section headings */
.heading{width:1200px;left:0;text-align:center;font-size:64px;font-weight:300;line-height:1.1}
.heading strong{font-weight:700}
.rule{width:66px;height:3px;background:linear-gradient(90deg,var(--orange) 0 60%,var(--blue) 60%)}

/* services */
.card{width:448px;color:var(--white);padding:0 70px}
.card .icon{width:200px;height:140px;border-radius:10px;margin-bottom:40px}
.c1 .icon,.c3 .icon{background:linear-gradient(150deg,#e8eef6 0%,#8fb2da 55%,#f08a2a 100%)}
.c2 .icon{background:linear-gradient(150deg,#ffffff 0%,#2a6bb0 60%,#0b3566 100%)}
.c4 .icon{background:linear-gradient(150deg,#e8eef6 0%,#8fb2da 55%,#f08a2a 100%)}
.card h3{font-size:25px;line-height:33px;font-weight:600}
.card a{display:inline-block;margin-top:26px;font-size:10px;font-weight:500;border-bottom:1px solid var(--white);padding-bottom:3px}
.c1{left:151px;top:851px;height:445px;background:linear-gradient(180deg,var(--navy) 0,#030f1f 100%);border-radius:14px 14px 0 0;padding-top:80px}
.c2{left:599px;top:927px;height:442px;background:linear-gradient(180deg,var(--orange) 0,var(--orange-deep) 100%);border-radius:0 14px 0 0;padding-top:80px}
.c3{left:151px;top:1296px;height:440px;background:linear-gradient(180deg,var(--green) 0,var(--green-deep) 100%);border-radius:0 0 0 14px;padding-top:80px}
.c4{left:599px;top:1369px;height:440px;background:linear-gradient(180deg,var(--blue) 0,#0b2b52 100%);border-radius:0 0 14px 14px;padding-top:80px}

/* fields */
.fields-bg{left:0;top:1790px;width:1200px;height:840px}
.fields-title{left:214px;top:2105px;font-size:64px;line-height:74px;font-weight:300}
.fields-title strong{font-weight:700;display:block}
.field{width:150px;text-align:center;font-size:10.5px;line-height:13px;color:#1e2a3a}
.field .ring{width:68px;height:68px;border-radius:50%;margin:0 auto 10px;border:3px solid #fff;box-shadow:0 2px 6px rgba(0,0,0,.15)}
.ring.b{background:var(--blue)}
.ring.o{background:var(--orange)}

/* team */
.team-photo{left:468px;top:2880px;width:265px;height:265px;border-radius:50%;background:linear-gradient(180deg,#c9d6e6 0%,#8d9aa6 45%,#4b5a3c 100%)}
.member{left:0;width:1200px;text-align:center}
.member-name{top:3160px;font-size:26px;font-weight:600}
.member-role{top:3198px;font-size:12px;color:var(--blue)}
.member-bio{top:3228px;left:440px;width:320px;font-size:12.5px;line-height:19px;color:var(--muted);text-align:center}
.badge{width:48px;height:48px}
.social{width:48px;height:48px;border-radius:50%;background:var(--blue);color:var(--white);font-size:9px;font-weight:500;display:flex;align-items:center;justify-content:center}

/* contact */
.contact-bg{left:0;top:3370px;width:1200px;height:790px}
.contact-title{left:224px;top:3712px;font-size:64px;line-height:74px;font-weight:300}
.contact-title strong{font-weight:700;display:block}
.form-card{left:585px;top:3524px;width:388px;height:520px;background:var(--white);border-radius:16px;padding:30px 34px 0 38px;box-shadow:0 8px 24px rgba(14,79,140,.08)}
.form-card h4{font-family:"Audiowide",sans-serif;font-weight:400;color:var(--blue);font-size:25px;margin-bottom:22px}
.form-card label{display:block;font-size:10px;color:var(--blue);margin-bottom:6px}
.field-box{height:54px;border:1px solid #e2e6ec;border-radius:6px;font-size:9.5px;color:#9aa3ae;padding:20px 14px 0;margin-bottom:22px}
.field-box.tall{height:110px}
.send{width:162px;height:48px;border-radius:6px;margin-left:154px;letter-spacing:1px}

/* blog */
.post{width:283px;height:391px;background:var(--pale-2);border-radius:0 0 12px 12px;overflow:hidden}
.post .ph{height:187px}
.post .body{padding:20px 28px}
.post .meta{font-size:9px;color:var(--muted)}
.post .meta span{color:var(--blue);margin-right:22px}
.post h5{font-size:12px;line-height:17px;font-weight:500;margin:14px 0 14px}
.post p{font-size:9.5px;line-height:14px;color:var(--muted)}

/* footer */
.footer-bg{left:0;top:4880px;width:1200px;height:369px}
.foot-brand{left:153px;top:5086px;font-size:38px}
.foot-brand .dot{width:34px;height:34px}
.foot-nav{top:5108px;right:152px;display:flex;gap:30px;color:var(--white);font-size:12px}
.foot-rule{left:151px;top:5174px;width:898px;height:1px;background:rgba(255,255,255,.2)}
.copy{left:151px;top:5200px;color:#a9b7c9;font-size:10px}
</style>
</head>
<body>

<!-- header -->
<svg class="abs hero-bg" viewBox="0 0 1200 620" preserveAspectRatio="none" aria-hidden="true">
  <defs><linearGradient id="hg" x1="0" y1="0" x2="0" y2="1"><stop offset="0" stop-color="#081d38"/><stop offset="1" stop-color="#0c2a4e"/></linearGradient></defs>
  <path d="M0 0H1200V450C1110 430 1020 470 940 520C820 590 700 470 560 520C460 560 410 610 300 600C190 590 90 500 0 440Z" fill="url(#hg)"/>
</svg>
<div class="abs brand site-brand"><span class="dot"></span>Zelmark</div>
<nav class="abs nav"><a>Service</a><a>Fields of expertise</a><a>Team</a><a>Contact</a><a>Blog</a><span class="flag" role="img" aria-label="English language flag"></span></nav>
<h1 class="abs hero-title">Custom Software <strong>Development</strong></h1>
<p class="abs hero-copy">Lorem ipsum dolor sit amet, consectetur adipiscing elit, sed do eiusmod tempor incididunt ut labore et dolore magna aliqua.</p>
<a class="abs btn hero-btn">Learn more</a>
<div class="abs hero-art" role="img" aria-label="Illustration of cloud, servers, monitors and laptop with gears"></div>

<!-- services -->
<h2 class="abs heading" style="top:690px">List of <strong>Services</strong></h2>
<div class="abs rule" style="left:567px;top:795px"></div>
<article class="abs card c1"><div class="icon" role="img" aria-label="Monitor with dashboards illustration"></div><h3>Custom Software<br>Development</h3><a>Learn More →</a></article>
<article class="abs card c2"><div class="icon" role="img" aria-label="Cloud computing illustration"></div><h3>Cloud Computing<br>Expertise</h3><a>Learn More →</a></article>
<article class="abs card c3"><div class="icon" role="img" aria-label="Consulting screens illustration"></div><h3>Consulting</h3><a>Learn More →</a></article>
<article class="abs card c4"><div class="icon" role="img" aria-label="Turn-key solutions devices illustration"></div><h3>Turn-Key Solutions</h3><a>Learn More →</a></article>

<!-- fields of expertise -->
<svg class="abs fields-bg" viewBox="0 0 1200 840" preserveAspectRatio="none" aria-hidden="true">
  <defs><linearGradient id="fg" x1="0" y1="0" x2="0" y2="1"><stop offset="0" stop-color="#f4f8fc"/><stop offset=".6" stop-color="#e2ecf7"/><stop offset="1" stop-color="#cddff1"/></linearGradient></defs>
  <path d="M0 20C150 90 300 0 500 50C700 110 900 20 1200 60V780C1050 740 950 820 760 800C560 770 420 720 250 760C150 790 60 820 0 840Z" fill="url(#fg)"/>
  <path d="M0 60C200 130 380 40 600 90C820 140 1000 60 1200 110V150C1000 110 820 190 600 140C380 90 200 180 0 110Z" fill="#ffffff" opacity=".5"/>
</svg>
<h2 class="abs fields-title">Fields of <strong>Expertise</strong></h2>
<div class="abs rule" style="left:214px;top:2278px"></div>
<div class="abs field" style="left:569px;top:2046px"><div class="ring b"></div>Industry 4.0</div>
<div class="abs field" style="left:721px;top:2046px"><div class="ring o"></div>Internet of Things (IoT)<br>+ Industrial IoT</div>
<div class="abs field" style="left:872px;top:2046px"><div class="ring b"></div>Automation</div>
<div class="abs field" style="left:569px;top:2192px"><div class="ring o"></div>Smart<br>manufacturing</div>
<div class="abs field" style="left:721px;top:2192px"><div class="ring b"></div>Cloud computing</div>
<div class="abs field" style="left:872px;top:2192px"><div class="ring o"></div>Supply chain<br>integration</div>
<div class="abs field" style="left:569px;top:2340px"><div class="ring b"></div>Digital twins</div>

<!-- team -->
<h2 class="abs heading" style="top:2640px;line-height:84px">My<br><strong>Teams</strong></h2>
<div class="abs rule" style="left:567px;top:2832px"></div>
<div class="abs team-photo" role="img" aria-label="Placeholder portrait of team member"></div>
<div class="abs member member-name">John Doe</div>
<div class="abs member member-role">President</div>
<p class="abs member-bio">Lorem ipsum dolor sit amet, consectetur adipiscing elit, sed do eiusmod tempor incididunt ut labore et dolore magna aliqua.</p>
<svg class="abs badge" style="left:535px;top:3316px" viewBox="0 0 48 48" role="img" aria-label="GVX certification badge"><path d="M24 2L44 13V35L24 46L4 35V13Z" fill="#2d3fb0"/></svg>
<div class="abs social" style="left:603px;top:3316px">Pellorin</div>

<!-- contact -->
<svg class="abs contact-bg" viewBox="0 0 1200 790" preserveAspectRatio="none" aria-hidden="true">
  <defs><linearGradient id="cg" x1="0" y1="0" x2="0" y2="1"><stop offset="0" stop-color="#f3f7fc"/><stop offset=".5" stop-color="#e2ecf7"/><stop offset="1" stop-color="#f3f7fc"/></linearGradient></defs>
  <path d="M0 40C200 0 400 80 650 40C880 0 1050 70 1200 30V740C1000 790 800 720 600 760C380 800 180 730 0 770Z" fill="url(#cg)"/>
</svg>
<h2 class="abs contact-title">Contact <strong>Us</strong></h2>
<div class="abs rule" style="left:224px;top:3885px"></div>
<form class="abs form-card">
  <h4>Get in touch!</h4>
  <label>Full name</label><div class="field-box">Enter your name</div>
  <label>Email</label><div class="field-box">Enter your email</div>
  <label>Message</label><div class="field-box tall">Enter your message</div>
  <div class="btn send">Send</div>
</form>

<!-- blog -->
<h2 class="abs heading" style="top:4230px">Our <strong>Blog</strong></h2>
<div class="abs rule" style="left:567px;top:4338px"></div>
<article class="abs post" style="left:151px;top:4396px"><div class="ph" role="img" aria-label="Photo of people working on a laptop" style="background:linear-gradient(135deg,#3d4a58,#8a8f8f,#2b3642)"></div><div class="body"><div class="meta"><span>Technology</span>June 04 2022</div><h5>Vexcom disables RCS ads in India following rampant spam</h5><p>Lorem ipsum dolor sit amet, consectetur adipiscing elit, sed do eiusmod tempor incididunt ut labore et dolore magna aliqua.</p></div></article>
<article class="abs post" style="left:458px;top:4396px"><div class="ph" role="img" aria-label="Photo of hands using a laptop" style="background:linear-gradient(135deg,#2a2620,#7d6b55,#1c1a17)"></div><div class="body"><div class="meta"><span>Technology</span>June 04 2022</div><h5>Vexcom disables RCS ads in India following rampant spam</h5><p>Lorem ipsum dolor sit amet, consectetur adipiscing elit, sed do eiusmod tempor incididunt ut labore et dolore magna aliqua.</p></div></article>
<article class="abs post" style="left:766px;top:4396px"><div class="ph" role="img" aria-label="Photo of a team working in an office" style="background:linear-gradient(135deg,#55504a,#a49a8c,#3b3630)"></div><div class="body"><div class="meta"><span>Technology</span>June 04 2022</div><h5>Vexcom disables RCS ads in India following rampant spam</h5><p>Lorem ipsum dolor sit amet, consectetur adipiscing elit, sed do eiusmod tempor incididunt ut labore et dolore magna aliqua.</p></div></article>

<!-- footer -->
<svg class="abs footer-bg" viewBox="0 0 1200 369" preserveAspectRatio="none" aria-hidden="true">
  <defs><linearGradient id="ftg" x1="0" y1="0" x2="0" y2="1"><stop offset="0" stop-color="#0c2a4e"/><stop offset="1" stop-color="#061a33"/></linearGradient></defs>
  <path d="M0 110C140 150 260 60 420 40C560 20 640 120 780 130C930 140 1050 30 1200 60V369H0Z" fill="url(#ftg)"/>
</svg>
<div class="abs brand foot-brand"><span class="dot"></span>Zelmark</div>
<nav class="abs foot-nav"><a>Service</a><a>Fields of expertise</a><a>Team</a><a>Contact</a><a>Blog</a></nav>
<div class="abs foot-rule"></div>
<p class="abs copy">Copyright © 2022 Zelmark Technologies</p>
<svg class="abs" style="left:962px;top:5192px;width:34px;height:34px" viewBox="0 0 48 48" role="img" aria-label="GVX certification badge"><path d="M24 2L44 13V35L24 46L4 35V13Z" fill="#2d3fb0"/></svg>
<div class="abs social" style="left:1015px;top:5192px;width:34px;height:34px;font-size:6px">Pellorin</div>

</body>
</html>
```